Stock Broking Firm - Web Design Project

We are looking at doing a full re-design of our home page and content page and moving the majority of our content over to DNN.

Phase 1 : Website redesign www.kpwealthdesk.com.au

The current design is too washed out, boring and has no call to action buttons.

Solution:

KP Wealthdesk is looking for a brighter/ cleaner redesign with a few stand out call to action buttons.

• Banner with logo across the top horizontally - Bright blue logo on white background similar to www.dailyledgerpress.com.au - CALL 1300 482 917 - Follow on Twitter / Facebook
• Horizontal menu bar - professional looking. - Home - About Us- Our Services - Membership - Open an Account - Become a member - Contact
• Below banner top left - large rotating banner - maybe zuvelo gallery style www.tallowhurst.com.au
• Right of rotating banner - Membership login
• Below members login - Register for Daily Market Report/ research blog - Large bright button / Name / Email / Phone / pop up??
• Below Register for daily market report - Market Indicies - RSS feed of delayed data from QNW see www.tallowhurst.com
• Below Market indicies - KP WEALTHDESK - Market Tweets ( feed from our twitter page)

Below Rotating Banner -

content area

Below content area - 4 large block buttons see www.greywickcapital.com.au ( hover over change colour)

Button 1 - EDUCATION - content - click here for more

Button 2 - Market Information and Research

Button 3 - Full service Broker - content brief - click here for more

Button 4 - Trade Commodities and Options

below buttons - small horizontal menu bar slightly different colour incl - Careers/ Partners / Legal Privacy FSG Site Map

Regards,
Colm Ashdown

Target Market(s)

35 - 65

Industry/Entity Type

Education

Requirements
Must have
• Follow brief above - large banner, call to action buttons, F.B. Twitter, Member login etc. 4 big buttons
Nice to have
• clean looking site similar to www.dailyledgerpress.com.au / not too busy. Corporate looking.
Should not have
• not too busy

```html
<!DOCTYPE html>
<html lang="en">
<head>
<meta charset="utf-8">
<title>KP Wealthdesk – Home</title>
<link rel="stylesheet" href="https://fonts.googleapis.com/css2?family=Noto+Sans:wght@400;700&display=swap">
<style>
  :root {
    --page-bg-top: #6f8fb0;
    --page-bg-bottom: #5a7a9e;
    --white: #ffffff;
    --logo-blue: #1d5a7a;
    --ink: #222222;
    --muted: #555555;
    --panel-bg: #eef0ea;
    --login-green-top: #8cc21c;
    --login-green-bottom: #4e8f08;
    --nav-top: #6b9bea;
    --nav-bottom: #2f62c4;
    --nav-divider: #8db0ee;
    --content-bg: #f2f2f2;
    --card-navy: #1f3f72;
    --card-navy-head: #152b4f;
    --card-cyan: #0a80c8;
    --card-black: #0a0a0a;
    --read-more: #8a8a8a;
    --footer-top: #7aa3f5;
    --footer-bottom: #3b6ad8;
    --footer-link: #2d3f66;
    --social: #2b8fd6;
  }
  * { box-sizing: border-box; margin: 0; padding: 0; }
  html, body { width: 1200px; height: 785px; overflow: hidden; }
  body {
    position: relative;
    font-family: "Noto Sans", sans-serif;
    background: linear-gradient(180deg, var(--page-bg-top), var(--page-bg-bottom));
  }
  .site-header {
    position: absolute; left: 59px; top: 0; width: 1089px; height: 94px;
    background: var(--white);
  }
  .brand { position: absolute; left: 22px; top: 14px; }
  .brand-name {
    display: flex; align-items: center; gap: 10px;
    font-size: 36px; line-height: 40px; color: var(--logo-blue); font-weight: 400;
  }
  .brand-mark { width: 30px; height: 30px; background: var(--logo-blue); }
  .brand-tagline { margin-left: 50px; font-size: 9px; line-height: 11px; color: var(--muted); text-align: right; width: 230px; }
  .phone {
    position: absolute; left: 502px; top: 24px;
    display: flex; align-items: center; gap: 4px;
    font-size: 24px; color: var(--ink);
  }
  .social { position: absolute; left: 970px; top: 28px; display: flex; gap: 16px; }
  .social a { width: 31px; height: 31px; border-radius: 3px; background: var(--social); display: block; }

  .hero {
    position: absolute; left: 59px; top: 100px; width: 842px; height: 278px; border-radius: 5px;
    background: radial-gradient(ellipse at 40% 45%, #3b8cf2 0%, #1a5fd4 45%, #0b2f8f 100%);
  }

  .login {
    position: absolute; left: 909px; top: 101px; width: 236px; height: 274px;
    background: var(--panel-bg); border-radius: 4px; padding: 2px;
  }
  .login-title {
    height: 48px; border-radius: 4px; padding-left: 22px;
    background: linear-gradient(180deg, var(--login-green-top), var(--login-green-bottom));
    color: var(--white); font-size: 15px; line-height: 48px;
  }
  .login label { display: block; margin: 12px 0 3px 12px; font-size: 14px; color: var(--ink); }
  .login label + .field { margin-top: 0; }
  .field {
    display: block; width: 209px; height: 37px; margin-left: 12px;
    background: var(--white); border: 1px solid #b8c4c0;
  }
  .login-button {
    position: absolute; right: 30px; top: 191px; width: 73px; height: 39px; border-radius: 4px;
    background: linear-gradient(180deg, var(--login-green-top), var(--login-green-bottom));
    color: var(--white); font-size: 14px; line-height: 39px; text-align: center;
  }
  .login-links { position: absolute; left: 24px; top: 244px; font-size: 11px; color: var(--ink); }
  .login-links strong { font-size: 15px; }

  .main-nav {
    position: absolute; left: 59px; top: 387px; width: 1089px; height: 46px;
    background: linear-gradient(180deg, var(--nav-top), var(--nav-bottom));
    display: flex;
  }
  .main-nav a {
    color: var(--white); text-decoration: none; font-size: 15px; line-height: 46px; text-align: center;
    border-right: 2px solid var(--nav-divider);
  }
  .main-nav a:last-child { border-right: none; }

  .content { position: absolute; left: 59px; top: 433px; width: 1089px; height: 276px; background: var(--content-bg); }
  .feature {
    position: absolute; top: 16px; width: 255px; height: 240px;
    background: var(--card-navy); border-radius: 4px 4px 0 0; color: var(--white);
  }
  .feature-title {
    height: 52px; border-radius: 4px; background: var(--card-navy-head);
    font-size: 16px; font-weight: 700; line-height: 50px; text-align: center;
  }
  .feature p { padding: 8px 14px 0 14px; font-size: 13px; line-height: 19px; }
  .feature-more {
    position: absolute; left: 0; bottom: 0; width: 100%; height: 23px;
    background: var(--card-black); color: var(--read-more);
    font-size: 13px; line-height: 23px; text-align: center;
  }
  .feature.is-active { background: var(--card-cyan); }
  .feature.is-active .feature-title { background: var(--card-black); }
  .feature.is-active p { padding-left: 20px; }

  .site-footer {
    position: absolute; left: 59px; top: 709px; width: 1089px; height: 76px;
    background: linear-gradient(180deg, var(--footer-top), var(--footer-bottom));
    display: flex; justify-content: center; gap: 28px; padding-top: 31px;
  }
  .site-footer a { color: var(--footer-link); font-size: 13px; text-decoration: none; }
  .site-footer a.current { color: var(--white); }
</style>
</head>
<body>
  <header class="site-header">
    <div class="brand">
      <div class="brand-name"><span class="brand-mark"></span>KP Wealthdesk</div>
      <div class="brand-tagline">shares | options | commodities | foreign exchange<br>ABN 52 307 614 829 | licence no 527 306</div>
    </div>
    <div class="phone">
      <svg width="42" height="48" viewBox="0 0 42 48" aria-hidden="true">
        <path d="M10 4 L17 4 L19 14 L14 18 C16 26 20 32 26 36 L31 31 L39 36 L37 44 C22 44 6 28 6 10 Z" fill="none" stroke="#222" stroke-width="2.2" stroke-linejoin="round"/>
      </svg>
      <span>1300 482 917</span>
    </div>
    <nav class="social" aria-label="Follow us">
      <a href="#" aria-label="Social link"></a>
      <a href="#" aria-label="Social link"></a>
    </nav>
  </header>

  <div class="hero" role="img" aria-label="Rotating banner: blue stock market ticker photograph"></div>

  <aside class="login">
    <div class="login-title">Members Login</div>
    <label>Username</label>
    <span class="field"></span>
    <label>Password</label>
    <span class="field"></span>
    <div class="login-button">Login</div>
    <div class="login-links"><strong>Register</strong>&nbsp; / &nbsp;Forgot password</div>
  </aside>

  <nav class="main-nav">
    <a href="#" style="width:148px">Home</a>
    <a href="#" style="width:124px">About Us</a>
    <a href="#" style="width:148px">Our Services</a>
    <a href="#" style="width:153px">Membership</a>
    <a href="#" style="width:191px">Open an Account</a>
    <a href="#" style="width:183px">Become a member</a>
    <a href="#" style="width:142px">Contact</a>
  </nav>

  <main class="content">
    <section class="feature is-active" style="left:14px">
      <h2 class="feature-title">Education</h2>
      <p>Lorem ipsum dolor sit amet, consec­tetuer adipi scing elit, sed diam non­ummy ipsum dolor. Dolor sit amet, consectetuer adipiscing elit, sed diam nonummy ipsum dolor. Lorem ipsum dolor sit amet, consectetuer adipisc­ing elit, sed diam nonummy ipsum dolor.</p>
      <div class="feature-more">Read More</div>
    </section>
    <section class="feature" style="left:282px">
      <h2 class="feature-title">Market Information</h2>
      <p>Lorem ipsum dolor sit amet, consec­tetuer adipi scing elit, sed diam non­ummy ipsum dolor. Dolor sit amet, consectetuer adipiscing elit, sed diam nonummy ipsum dolor. Lorem ipsum dolor sit amet, consectetuer adipisc­ing elit, sed diam nonummy ipsum dolor.</p>
      <div class="feature-more">Read More</div>
    </section>
    <section class="feature" style="left:550px">
      <h2 class="feature-title">Full service Broker</h2>
      <p>Lorem ipsum dolor sit amet, consec­tetuer adipi scing elit, sed diam non­ummy ipsum dolor. Dolor sit amet, consectetuer adipiscing elit, sed diam nonummy ipsum dolor. Lorem ipsum dolor sit amet, consectetuer adipisc­ing elit, sed diam nonummy ipsum dolor.</p>
      <div class="feature-more">Read More</div>
    </section>
    <section class="feature" style="left:818px">
      <h2 class="feature-title">Trade Commodities</h2>
      <p>Lorem ipsum dolor sit amet, consec­tetuer adipi scing elit, sed diam non­ummy ipsum dolor. Dolor sit amet, consectetuer adipiscing elit, sed diam nonummy ipsum dolor. Lorem ipsum dolor sit amet, consectetuer adipisc­ing elit, sed diam nonummy ipsum dolor.</p>
      <div class="feature-more">Read More</div>
    </section>
  </main>

  <footer class="site-footer">
    <a href="#">Careers</a>
    <a href="#" class="current">Partners</a>
    <a href="#">Legal Privacy</a>
    <a href="#">FSG</a>
    <a href="#">Site Map</a>
  </footer>
</body>
</html>
```